Harbor Advance, Inc.

We need a website design for a new company based in Orange County, CA but will be serving client's throughout all of California. We provide non-recourse loans/ pre-litigation funding for client's in personal injury and employment cases. Generally, if a client has an active case and they need money for cost of living, the client will contact a company like ours to provide a loan. We would like to see designs that are sleek, simple and easy to use. The final design should communicate trustworthiness, financial safety and promptness.

Hi, I like KW's designs. I am having him work on a hybrid of two of his designs. We had a little miscommunication, but we are almost there. Best, Ned

```html
<!DOCTYPE html>
<html lang="en">
<head>
<meta charset="utf-8">
<title>Harbor Advance Inc – Non-recourse loans</title>
<link href="https://fonts.googleapis.com/css2?family=Open+Sans:wght@400;600;700&family=Poppins:wght@400;500;600&family=Roboto+Condensed:wght@400;700&display=swap" rel="stylesheet">
<style>
:root{
  --blue:#1f6db0;
  --blue-dark:#155a94;
  --blue-band:#2d7fc4;
  --ink:#1b1b1b;
  --text:#444;
  --muted:#6a6a6a;
  --grey-bg:#e9e9e9;
  --card-grey:#e6e6e6;
  --footer:#0f1013;
  --footer-bottom:#08090b;
  --white:#fff;
}
*{box-sizing:border-box;margin:0;padding:0}
html,body{width:1200px;height:4245px;overflow:hidden}
body{position:relative;background:var(--white);font-family:"Open Sans",Arial,sans-serif;color:var(--text)}
.abs{position:absolute}
section,header,footer{position:absolute;left:0;width:1200px}
.heading{font-family:"Roboto Condensed",Arial,sans-serif;font-weight:400;color:var(--ink);font-size:44px;text-align:center;width:1200px;left:0;position:absolute}

/* header */
.site-header{top:0;height:148px;border-top:6px solid var(--blue);background:var(--white)}
.brand-mark{left:144px;top:26px;width:56px;height:56px;border-radius:50%;background:var(--blue)}
.brand-name{left:70px;top:90px;width:204px;text-align:center;font-family:"Roboto Condensed",Arial,sans-serif;font-weight:700;font-size:21px;color:var(--ink)}
.phone{left:632px;top:40px;font-size:19px;color:var(--ink);display:flex;align-items:center;gap:6px}
.search{left:800px;top:37px;width:185px;height:34px;border:1px solid #bbb;font-size:14px;padding:8px 10px;color:#333}
.search svg{position:absolute;right:9px;top:9px}
.enquire{left:997px;top:37px;width:113px;height:34px;background:var(--blue);color:#fff;font-weight:700;font-size:15px;text-align:center;line-height:34px}
.nav a{position:absolute;top:93px;font-size:17px;color:#333;text-decoration:none}
.nav a.active{color:var(--blue)}

/* hero */
.hero{top:148px;height:594px}
.hero-photo{inset:0;background:linear-gradient(90deg,#3a2a1f 0%,#6b5440 30%,#a58a6c 60%,#d7c9b6 100%)}
.hero-shade{inset:0;background:linear-gradient(90deg,rgba(0,0,0,.35),rgba(0,0,0,0) 55%)}
.hero h1{left:85px;top:168px;font-family:"Poppins",Arial,sans-serif;font-weight:400;font-size:46px;color:#fff;line-height:1.2}
.hero h2{left:85px;top:228px;font-family:"Poppins",Arial,sans-serif;font-weight:600;font-size:47px;color:#fff}
.hero p{left:85px;top:296px;font-family:"Poppins",Arial,sans-serif;font-size:21px;color:#fff}
.btn{background:var(--blue);color:#fff;font-family:"Poppins",Arial,sans-serif;font-size:17px;text-align:center}
.hero .btn{left:88px;top:357px;width:178px;height:44px;line-height:44px}
.slider-dot{top:474px;width:22px;height:22px;border-radius:50%;background:rgba(0,0,0,.5);border:1.5px solid #fff}
.slider-dot svg{position:absolute;left:5px;top:5px}

/* services */
.services{top:742px;height:617px}
.services .heading{top:98px}
.svc{top:209px;width:323px;height:318px;text-align:center}
.svc.featured{background:var(--card-grey);box-shadow:0 3px 8px rgba(0,0,0,.2)}
.svc .icon{position:absolute;left:111px;top:29px;width:100px;height:100px;border-radius:50%;background:radial-gradient(circle at 40% 35%,#3c8fd2,var(--blue-dark));box-shadow:0 3px 6px rgba(0,0,0,.3)}
.svc .icon svg{position:absolute;left:30px;top:30px}
.svc h3{position:absolute;top:154px;width:100%;font-size:20px;font-weight:600;color:var(--ink)}
.svc p{position:absolute;top:200px;left:44px;width:235px;font-size:14.5px;line-height:1.6}

/* about */
.about{top:1359px;height:535px}
.about-photo{inset:0;background:linear-gradient(100deg,#cfd0cc 0%,#b9a38a 22%,#8f5a3b 40%,#7a4730 70%,#6e3f2a 100%)}
.about-shade{left:540px;top:0;width:660px;height:535px;background:rgba(90,45,25,.35)}
.about h2{left:589px;top:100px;font-family:"Roboto Condensed",Arial,sans-serif;font-weight:400;font-size:44px;color:#fff}
.about .lead{left:589px;top:174px;width:530px;font-size:15px;line-height:1.75;color:#fff}
.about ul{left:589px;top:248px;list-style:none;color:#fff;font-size:16px}
.about li{height:45px;display:flex;align-items:flex-start;gap:10px}
.about li svg{flex:none;margin-top:3px}

/* cases */
.cases{top:1894px;height:718px}
.cases .heading{top:138px}
.case{top:240px;width:317px;height:382px;background:#fff;box-shadow:0 2px 10px rgba(0,0,0,.22);text-align:center}
.case .photo{position:absolute;left:14px;top:12px;width:289px;height:193px}
.case h3{position:absolute;top:232px;width:100%;font-size:23px;font-weight:600;color:var(--ink)}
.case p{position:absolute;top:282px;left:26px;width:265px;font-size:14px;line-height:1.6}
.case a{position:absolute;top:337px;width:100%;left:0;font-size:14.5px;color:var(--blue);text-decoration:none}

/* blog */
.blog{top:2612px;height:713px;background:var(--grey-bg)}
.blog .heading{top:80px}
.post{top:195px;width:497px;height:442px;background:#fff;box-shadow:0 1px 5px rgba(0,0,0,.12)}
.post .photo{position:absolute;left:0;top:0;width:497px;height:235px}
.post .date{position:absolute;left:38px;top:256px;font-size:14px;font-weight:700;color:var(--blue)}
.post h3{position:absolute;left:38px;top:285px;font-family:"Poppins",Arial,sans-serif;font-weight:400;font-size:21px;color:var(--ink)}
.post p{position:absolute;left:38px;top:326px;width:430px;font-size:13px;line-height:1.7;color:var(--muted)}
.post .more{position:absolute;left:38px;top:384px;font-size:13px;font-weight:700;color:#222;padding-bottom:6px;border-bottom:3px solid var(--blue)}

/* contact */
.contact{top:3325px;height:524px;background:linear-gradient(180deg,#2f7fc3 0%,#2873b5 60%,#1e5f9b 100%)}
.contact .heading{top:70px;color:#fff}
.field{height:56px;background:#fff;border:1px solid #d0d0d0;font-size:16px;color:#333;padding:16px 16px}
.field.select svg{position:absolute;right:18px;top:24px}
.contact .submit{left:509px;top:413px;width:182px;height:52px;background:#1e1e1e;color:#fff;font-weight:700;font-size:22px;text-align:center;line-height:52px;border-radius:2px}
.contact-edge{top:3849px;height:11px;background:var(--blue-band)}

/* footer */
.site-footer{top:3860px;height:385px;background:var(--footer);color:#fff}
.foot-mark{left:156px;top:100px;width:56px;height:56px;border-radius:50%;background:var(--blue)}
.foot-name{left:84px;top:164px;width:200px;text-align:center;font-family:"Roboto Condensed",Arial,sans-serif;font-weight:700;font-size:21px}
.social{top:216px;width:30px;height:30px;border-radius:50%;background:#fff}
.foot-col h4{position:absolute;font-size:19px;font-weight:400;letter-spacing:.5px}
.foot-col a{position:absolute;font-size:15px;color:#fff;text-decoration:none}
.info{font-size:13px;line-height:1.5}
.info strong{font-size:14px;font-weight:700;display:block}
.copyright{left:0;top:314px;width:1200px;height:71px;background:var(--footer-bottom);text-align:center;line-height:71px;font-size:14px;color:#9a9a9a}
</style>
</head>
<body>

<header class="site-header">
  <div class="abs brand-mark"></div>
  <div class="abs brand-name">HARBOR ADVANCE INC</div>
  <div class="abs phone">
    <svg width="16" height="16" viewBox="0 0 24 24"><path fill="#1b1b1b" d="M6.6 10.8a15 15 0 0 0 6.6 6.6l2.2-2.2a1 1 0 0 1 1-.25 11.4 11.4 0 0 0 3.6.57 1 1 0 0 1 1 1V20a1 1 0 0 1-1 1A17 17 0 0 1 3 4a1 1 0 0 1 1-1h3.5a1 1 0 0 1 1 1c0 1.25.2 2.45.57 3.57a1 1 0 0 1-.25 1z"/></svg>
    (08) 5550 0142
  </div>
  <div class="abs search">Search
    <svg width="15" height="15" viewBox="0 0 24 24"><circle cx="10" cy="10" r="6.5" fill="none" stroke="#333" stroke-width="3"/><path d="M15 15l6 6" stroke="#333" stroke-width="3"/></svg>
  </div>
  <div class="abs enquire">ENQUIRE</div>
  <nav class="nav">
    <a class="active" style="left:417px">Home</a>
    <a style="left:530px">About us</a>
    <a style="left:666px">Services</a>
    <a style="left:797px">Loan</a>
    <a style="left:900px">Articles</a>
    <a style="left:1024px">Contact us</a>
  </nav>
</header>

<section class="hero">
  <div class="abs hero-photo" role="img" aria-label="Photo of a woman in glasses reading loan documents at a table"></div>
  <div class="abs hero-shade"></div>
  <h1 class="abs">Harbor Advance Inc</h1>
  <h2 class="abs">Non-recourse loans</h2>
  <p class="abs">Neque porro quisquam est qui dolorem</p>
  <div class="abs btn">Get Started Now</div>
  <div class="abs slider-dot" style="left:90px"><svg width="10" height="10" viewBox="0 0 10 10"><path d="M6.5 1.5L3 5l3.5 3.5" fill="none" stroke="#fff" stroke-width="2"/></svg></div>
  <div class="abs slider-dot" style="left:117px"><svg width="10" height="10" viewBox="0 0 10 10"><path d="M3.5 1.5L7 5 3.5 8.5" fill="none" stroke="#fff" stroke-width="2"/></svg></div>
</section>

<section class="services">
  <h2 class="heading">Our Services</h2>
  <div class="abs svc" style="left:81px">
    <div class="icon"><svg width="40" height="40" viewBox="0 0 40 40" fill="none" stroke="#fff" stroke-width="2"><rect x="9" y="5" width="22" height="30"/><path d="M14 13h12M14 19h12M14 25h8"/></svg></div>
    <h3>Neque porro</h3>
    <p>It is a long established fact that a reader will be distracted by the readable content of a page</p>
  </div>
  <div class="abs svc featured" style="left:433px">
    <div class="icon"><svg width="40" height="40" viewBox="0 0 40 40" fill="none" stroke="#fff" stroke-width="2"><rect x="5" y="7" width="30" height="20"/><path d="M16 33h8M20 27v6M12 20l5-5 4 4 7-7"/></svg></div>
    <h3>Dolorem ipsum</h3>
    <p>It is a long established fact that a reader will be distracted by the readable content of a page when looking</p>
  </div>
  <div class="abs svc" style="left:779px">
    <div class="icon"><svg width="40" height="40" viewBox="0 0 40 40" fill="none" stroke="#fff" stroke-width="2"><circle cx="25" cy="10" r="4"/><circle cx="14" cy="14" r="3"/><path d="M4 30h8l8 3 14-7-3-3-9 4h-6M4 24h7l6 2"/></svg></div>
    <h3 style="top:160px">Porro quisquam</h3>
    <p style="top:206px">It is a long established fact that a reader will be distracted by the readable content of a page when looking</p>
  </div>
</section>

<section class="about">
  <div class="abs about-photo" role="img" aria-label="Photo of hands signing a contract on a clipboard on a wooden desk"></div>
  <div class="abs about-shade"></div>
  <h2 class="abs">About us</h2>
  <p class="abs lead">The point of using Lorem Ipsum is that it has a more-or-less normal distribution of letters, as opposed to using 'Content here.</p>
  <ul class="abs">
    <li><svg width="16" height="16" viewBox="0 0 16 16"><circle cx="8" cy="8" r="8" fill="#fff"/><path d="M6.5 4.5L10 8l-3.5 3.5" fill="none" stroke="#7a4730" stroke-width="2"/></svg>Lorem ipsum dolor sit amet, consectetur adipiscing elit.</li>
    <li><svg width="16" height="16" viewBox="0 0 16 16"><circle cx="8" cy="8" r="8" fill="#fff"/><path d="M6.5 4.5L10 8l-3.5 3.5" fill="none" stroke="#7a4730" stroke-width="2"/></svg>Sed vel dui vel diam ultricies dignissim.</li>
    <li><svg width="16" height="16" viewBox="0 0 16 16"><circle cx="8" cy="8" r="8" fill="#fff"/><path d="M6.5 4.5L10 8l-3.5 3.5" fill="none" stroke="#7a4730" stroke-width="2"/></svg>Mauris eget purus eget ante congue egestas at ac mi</li>
    <li><svg width="16" height="16" viewBox="0 0 16 16"><circle cx="8" cy="8" r="8" fill="#fff"/><path d="M6.5 4.5L10 8l-3.5 3.5" fill="none" stroke="#7a4730" stroke-width="2"/></svg>Aliquam pretium quam rhoncus lectus porta euismod.</li>
    <li><svg width="16" height="16" viewBox="0 0 16 16"><circle cx="8" cy="8" r="8" fill="#fff"/><path d="M6.5 4.5L10 8l-3.5 3.5" fill="none" stroke="#7a4730" stroke-width="2"/></svg>Vestibulum non lacus a massa vestibulum mattis.</li>
  </ul>
</section>

<section class="cases">
  <h2 class="heading">We Do Services For</h2>
  <div class="abs case" style="left:102px">
    <div class="photo" role="img" aria-label="Photo of an injured client meeting a lawyer at a desk" style="background:linear-gradient(135deg,#c9d3dc,#8aa1b5 50%,#d8d2c8)"></div>
    <h3>Personal injury</h3>
    <p>It is a long established fact that reader will be distracted the readable the point</p>
    <a>Read More »</a>
  </div>
  <div class="abs case" style="left:444px">
    <div class="photo" role="img" aria-label="Photo of an employee with a neck brace in a meeting" style="background:linear-gradient(135deg,#a7a7ad,#6b5a60 50%,#c7c2c4)"></div>
    <h3>Employment cases</h3>
    <p>It is a long established fact that reader will be distracted the readable the point</p>
    <a>Read More »</a>
  </div>
  <div class="abs case" style="left:787px">
    <div class="photo" role="img" aria-label="Photo of a couple reviewing papers together" style="background:linear-gradient(135deg,#9aa4a6,#6f7f86 50%,#b48a86)"></div>
    <h3>Quisquam est qui</h3>
    <p>It is a long established fact that reader will be distracted the readable the point</p>
    <a>Read More »</a>
  </div>
</section>

<section class="blog">
  <h2 class="heading">Latest Blog</h2>
  <article class="abs post" style="left:90px">
    <div class="photo" role="img" aria-label="Photo of a coastal town on a hillside above a beach" style="background:linear-gradient(180deg,#5f9fd6 0%,#9cc4e3 30%,#8a9b6e 55%,#c8b590 80%,#4f88a8 100%)"></div>
    <div class="date">MARCH 20, 2019</div>
    <h3>Neque porro quisquam est qui</h3>
    <p>Praesent elementum elit at tellus nec ultricies sit amet porttitor mattis enim In massa libero interdum nec interdum vel blandi</p>
    <div class="more">READ MORE</div>
  </article>
  <article class="abs post" style="left:608px">
    <div class="photo" role="img" aria-label="Photo of a modern glass building with palm trees" style="background:linear-gradient(180deg,#5c94d1 0%,#a9c9ea 40%,#c9cfd4 60%,#6f8a5a 85%,#9aa093 100%)"></div>
    <div class="date">MARCH 20, 2019</div>
    <h3>Dolorem ipsum quia dolor sit amet</h3>
    <p>Praesent elementum elit at tellus nec ultricies sit amet porttitor mattis enim In massa libero interdum nec interdum</p>
    <div class="more">READ MORE</div>
  </article>
</section>

<section class="contact">
  <h2 class="heading">Contact Us</h2>
  <div class="abs field" style="left:93px;top:168px;width:320px">First Name</div>
  <div class="abs field" style="left:436px;top:168px;width:320px">Surname</div>
  <div class="abs field" style="left:778px;top:168px;width:320px">Email Address</div>
  <div class="abs field" style="left:93px;top:244px;width:320px">Contact number</div>
  <div class="abs field select" style="left:436px;top:244px;width:320px">State
    <svg width="12" height="8" viewBox="0 0 12 8"><path d="M0 0h12L6 8z" fill="#333"/></svg>
  </div>
  <div class="abs field" style="left:778px;top:244px;width:320px">Postcode</div>
  <div class="abs field" style="left:93px;top:318px;width:1005px">Enquiry</div>
  <div class="abs submit">Submit</div>
</section>
<div class="abs contact-edge" style="left:0;width:1200px"></div>

<footer class="site-footer">
  <div class="abs foot-mark"></div>
  <div class="abs foot-name">HARBOR ADVANCE INC</div>
  <div class="abs social" style="left:95px" aria-label="Social link"></div>
  <div class="abs social" style="left:149px" aria-label="Social link"></div>
  <div class="abs social" style="left:206px" aria-label="Social link"></div>
  <div class="abs social" style="left:260px" aria-label="Social link"></div>

  <div class="foot-col">
    <h4 style="left:447px;top:80px">CONTACT US</h4>
    <svg class="abs" style="left:443px;top:133px" width="18" height="24" viewBox="0 0 18 24"><path d="M9 1a7 7 0 0 0-7 7c0 5 7 14 7 14s7-9 7-14a7 7 0 0 0-7-7z" fill="none" stroke="#fff" stroke-width="1.6"/><circle cx="9" cy="8" r="2.5" fill="none" stroke="#fff" stroke-width="1.6"/></svg>
    <div class="abs info" style="left:475px;top:132px"><strong>ADDRESS</strong>118 Wharf Lane Seaview,<br>Coastal Region</div>
    <svg class="abs" style="left:443px;top:210px" width="18" height="18" viewBox="0 0 24 24"><path fill="none" stroke="#fff" stroke-width="2" d="M6.6 10.8a15 15 0 0 0 6.6 6.6l2.2-2.2a1 1 0 0 1 1-.25 11.4 11.4 0 0 0 3.6.57 1 1 0 0 1 1 1V20a1 1 0 0 1-1 1A17 17 0 0 1 3 4a1 1 0 0 1 1-1h3.5a1 1 0 0 1 1 1c0 1.25.2 2.45.57 3.57a1 1 0 0 1-.25 1z"/></svg>
    <div class="abs info" style="left:475px;top:208px"><strong>PHONE NUMBER</strong>(08) 5550 0142</div>
  </div>
  <div class="foot-col">
    <h4 style="left:761px;top:80px">ABOUT</h4>
    <a style="left:763px;top:126px">Home</a>
    <a style="left:763px;top:159px">About Us</a>
    <a style="left:763px;top:191px">Services</a>
    <a style="left:763px;top:224px">Help us</a>
  </div>
  <div class="foot-col">
    <h4 style="left:979px;top:80px">RESOURCES</h4>
    <a style="left:981px;top:126px">Support</a>
    <a style="left:981px;top:159px">Why Us</a>
    <a style="left:981px;top:191px">Testimonials</a>
    <a style="left:981px;top:224px">FAQ</a>
  </div>
  <div class="abs copyright">© 2019 Company Name &nbsp;All right reserved</div>
</footer>

</body>
</html>
```